Wordpress design for my private practice website - Psychotherapist

I would like a simple, clean, and elegant design for my private practice website. I work with both adults and children so I'd like it to appeal to both. However, since parents make the choice as to where to send their child for therapy, I want it to appeal to adults more. I would like the pictures on the site to have a calming effect - maybe using sand and water and rocks. I am attaching files with my company logo. I would also like my name incorporated into the header - Rosalind Vantreece, LCSW, Registered Play Therapist. I've also uploaded a picture of myself for my About Page.

I like the design of these 2 website and want something similar:
www.drmaribelostrand.com
www.harrowgate-lisk.com

I would like a home page that highlights a calming graphic across the entire top of the page as well as my practice logo and my name.

I'd like a link to social media sites on the top of the homepage - facebook, pinterest.

I want a simple bar across the top with the following tabs:
Home
About Me (subtabs Who I Am, Specialties and Approach)
Counseling Services (subtabs Individual Counseling, Play Therapy, Sandplay Therapy,)
Fees
FAQs
Contact Me (would love this to be a fill in the blank contact form that sends info to my email address - should include name, phone number, email and a comment box for more information requested)
Blog (this will link with another wordpress blog)

Target Market(s)

Parents of children under age 12 with behavioral problems or are dealing with the breakup of their family through divorce - looking for someone to work with their young child. I also work with Adults that are overwhelmed and worried - often women that have many life stressors and are feeling burnt out on life and meeting everyone's needs. Families going through some type of trauma, including divorce or grief work. I also work with individuals going through a transition of religious beliefs - often exiting the religion of their youth and undergoing a crisis of faith at midlife.

Industry/Entity Type

Mental Health

Contact Information for Business Card

Rosalind Vantreece, LCSW
Registered Play Therapist
4815 Bellhaven Court
Idaho Falls, Idaho 83404
(208)555-7162
www.stillbrookwellness.com

On the opposite side, I'd like an appointment reminder area - with the following text:

Your next appointment is
_____/______/______ at ______am/pm
Please give 24 hrs notice if you need to cancel your appointment.

Coding

Coded - Design and coding required

Number of Pages Required

5+ page

Font styles to use
Sans Serif

Colors
33a6d7
9bcb3c
0355a3

Requirements
Must have
• I'd like it to be a wordpress site. I'm such a newby at web design - but I need to be able to add content and manage the site myself once it is up and running.
Nice to have
• I like the design of these 2 websites and want something similar:
• www.drmaribelostrand.com
• www.harrowgate-lisk.com
• They are clean, easy to navigate and calming.
Should not have
• Should not look like a childcare website.

```html
<!DOCTYPE html>
<html lang="en">
<head>
<meta charset="UTF-8">
<title>Rosalind Vantreece — LCSW, Registered Play Therapist</title>
<link rel="stylesheet" href="https://fonts.googleapis.com/css2?family=Lato:wght@400;700&family=Montserrat:wght@700&family=Pinyon+Script&family=Roboto+Slab:wght@400&display=swap">
<style>
  :root {
    --ink: #1c1c1c;
    --muted: #8a8a8a;
    --brand-blue: #2e6a9e;
    --link-blue: #2f6ea5;
    --logo-grey: #6d7479;
    --sky-top: #dde8f4;
    --sea: #c9dbe6;
    --sand-light: #f3ece3;
    --dune-top: #efd9cc;
    --dune-bottom: #f2cbb2;
    --white: #ffffff;
  }
  * { box-sizing: border-box; margin: 0; padding: 0; }
  html, body { width: 855px; height: 1200px; overflow: hidden; }
  body { font-family: "Lato", sans-serif; color: var(--ink); background: var(--white); position: relative; }

  .hero {
    position: absolute; left: 0; top: 0; width: 855px; height: 483px;
    background: linear-gradient(180deg, var(--sky-top) 0%, #e3ecf5 38%, var(--sea) 46%, #dfe6e8 58%, var(--sand-light) 80%, #f6efe6 100%);
  }
  .brand {
    position: absolute; left: 56px; top: 52px;
    display: flex; align-items: center; gap: 10px;
    font-size: 15px; letter-spacing: 3.5px; color: var(--logo-grey); font-weight: 400;
  }
  .brand-dot { width: 14px; height: 14px; border-radius: 50%; background: var(--brand-blue); }
  .menu-toggle {
    position: absolute; left: 741px; top: 36px;
    display: flex; align-items: center; gap: 9px;
    font-size: 11px; color: var(--ink); letter-spacing: 0.3px;
  }
  .hero-title {
    position: absolute; left: 0; width: 855px; top: 205px; text-align: center;
  }
  .hero-title h1 {
    font-family: "Pinyon Script", cursive; font-weight: 400; font-size: 38px; color: #111;
  }
  .hero-title p {
    margin-top: 2px; font-size: 13.5px; letter-spacing: 3px; color: #555;
  }

  .about {
    position: absolute; left: 0; top: 483px; width: 855px; height: 420px; background: var(--white);
  }
  .about-photo {
    position: absolute; left: 0; top: 0; width: 286px; height: 420px;
    background: linear-gradient(135deg, #d9c07a 0%, #c9b27a 35%, #8a9a55 75%, #5f7a3a 100%);
  }
  .about-copy { position: absolute; left: 386px; top: 100px; width: 390px; }
  .about-copy h2 { font-family: "Montserrat", sans-serif; font-size: 14.5px; font-weight: 700; color: #111; }
  .about-copy .lead {
    margin-top: 17px; font-size: 11.5px; line-height: 19.2px; letter-spacing: 1.1px; color: var(--muted);
  }
  .about-copy .invite {
    margin-top: 35px; font-size: 10.5px; line-height: 15px; letter-spacing: 0.9px; color: #111;
  }
  .contact-line { margin-top: 22px; display: flex; gap: 24px; font-size: 10.5px; color: #555; }
  .contact-line span { display: flex; align-items: center; gap: 8px; }

  .contact {
    position: absolute; left: 0; top: 903px; width: 855px; height: 297px;
    background: linear-gradient(170deg, #e8d8cf 0%, var(--dune-top) 40%, var(--dune-bottom) 100%);
  }
  .contact-note { position: absolute; top: 41px; width: 855px; text-align: center; font-size: 10px; color: #222; }
  .contact-form { position: absolute; left: 166px; top: 78px; width: 524px; }
  .field {
    border: 1px solid #222; border-radius: 11px; height: 22px; padding: 4px 9px;
    font-size: 10px; color: #222; background: transparent;
  }
  .row { display: flex; gap: 5px; }
  .row .field { flex: 1; }
  .field.message { margin-top: 4px; height: 74px; border-radius: 9px; }
  .submit {
    margin-top: 4px; height: 29px; border-radius: 15px; background: var(--brand-blue);
    color: var(--white); font-family: "Roboto Slab", serif; font-size: 11px; letter-spacing: 2.5px;
    display: flex; align-items: center; justify-content: center;
  }
  .footer { position: absolute; top: 252px; width: 855px; text-align: center; font-size: 10.5px; color: #222; }
  .footer a { color: var(--link-blue); text-decoration: none; }
</style>
</head>
<body>
  <header class="hero" role="img" aria-label="Soft beach scene of a family walking hand in hand along the shoreline">
    <div class="brand"><span class="brand-dot"></span>STILLBROOK WELLNESS</div>
    <nav class="menu-toggle">
      <svg width="16" height="10" viewBox="0 0 16 10"><path d="M0 1h16M0 5h16M0 9h16" stroke="#333" stroke-width="1"/></svg>
      MENU
    </nav>
    <div class="hero-title">
      <h1>Rosalind Vantreece</h1>
      <p>LCSW, Registered Play Therapist</p>
    </div>
  </header>

  <section class="about">
    <div class="about-photo" role="img" aria-label="Portrait of the therapist outdoors in golden grass"></div>
    <div class="about-copy">
      <h2>FIND YOUR STILLNESS</h2>
      <p class="lead">If you're looking for extra support and guidance through a challenging situation or you're just ready to move in a new direction in your life, I look forward to working with you to achieve your goals.</p>
      <p class="invite">Please call or email me for an individual, couples or family therapy consultation today.</p>
      <div class="contact-line">
        <span><svg width="7" height="11" viewBox="0 0 7 11"><rect x="0.6" y="0.6" width="5.8" height="9.8" rx="1.2" fill="none" stroke="#2e6a9e" stroke-width="1.2"/><circle cx="3.5" cy="8.6" r="0.7" fill="#2e6a9e"/></svg>(208)555-7162</span>
        <span><svg width="11" height="8" viewBox="0 0 11 8"><rect width="11" height="8" rx="1" fill="#2e6a9e"/><path d="M0.5 0.8 5.5 4.6 10.5 0.8" fill="none" stroke="#fff" stroke-width="0.9"/></svg>info@stillbrookwellness.com</span>
      </div>
    </div>
  </section>

  <section class="contact" role="img" aria-label="Soft close-up of sand dunes in warm peach tones">
    <p class="contact-note">would love this to be a fill in the blank contact form that sends info to my email address</p>
    <div class="contact-form">
      <div class="row">
        <div class="field">Name</div>
        <div class="field">Email Id</div>
      </div>
      <div class="field message">Message</div>
      <div class="submit">SUBMIT</div>
    </div>
    <p class="footer">© <a>STILLBROOK WELLNESS</a> - 2016. All Rights reserved.</p>
  </section>
</body>
</html>
```